DVK Webpage

We are a group dedicated to Paranormal research located in central Mississippi .. we are looking for an index page and a blank template so we can fill in and finish the rest. Would like links to include, Home, About us, Research, Contact us and More.. kind of like the look of the image uploaded .. also included is our logo

```html
<!DOCTYPE html>
<html lang="en">
<head>
<meta charset="utf-8">
<title>DVK – About Us</title>
<link rel="stylesheet" href="https://fonts.googleapis.com/css2?family=Arimo:wght@400;700&family=UnifrakturMaguntia&family=Oswald:wght@600&display=swap">
<style>
  :root {
    --night-deep: #0b1a2c;
    --night-mid: #1c3a5e;
    --night-fog: #3a5f8a;
    --bar-black: #000000;
    --panel-black: #000000;
    --frame-dark: #07080b;
    --nav-text: #d9d9d9;
    --body-text: #f2f2f2;
    --heading-silver: #d6d6d6;
    --tagline-grey: #a9abad;
    --crest-cream: #d9cfa6;
  }
  * { margin: 0; padding: 0; box-sizing: border-box; }
  html, body { width: 1200px; height: 689px; overflow: hidden; }
  body {
    position: relative;
    font-family: "Arimo", Arial, sans-serif;
    background: var(--night-deep);
  }
  .scene-backdrop {
    position: absolute; inset: 0;
    background:
      radial-gradient(ellipse at 72% 40%, var(--night-fog) 0%, transparent 55%),
      radial-gradient(ellipse at 20% 85%, #0e2036 0%, transparent 60%),
      linear-gradient(180deg, var(--night-mid) 0%, #234670 45%, #13273f 100%);
  }
  .top-bar {
    position: absolute; top: 0; left: 0;
    width: 1200px; height: 25px;
    background: var(--bar-black);
  }
  .top-bar a {
    position: absolute; top: 4px;
    color: var(--nav-text);
    font-size: 15px; line-height: 17px;
    text-decoration: none;
    transform: translateX(-50%);
    white-space: nowrap;
  }
  .top-bar .home-cross { top: 5px; }
  .crest {
    position: absolute; left: 52px; top: 220px;
    width: 230px; height: 90px;
    display: flex; align-items: center; justify-content: center; gap: 14px;
  }
  .crest-dot {
    width: 26px; height: 26px; border-radius: 50%;
    background: var(--crest-cream);
  }
  .crest-name {
    font-family: "Arimo", Arial, sans-serif;
    font-weight: 700; font-size: 78px; line-height: 1;
    color: var(--crest-cream);
  }
  .frame-ornament {
    position: absolute; left: 622px; top: 50px;
    width: 440px; height: 490px;
    background: var(--frame-dark);
    border-radius: 6px;
  }
  .about-panel {
    position: absolute; left: 655px; top: 85px;
    width: 370px; height: 420px;
    background: var(--panel-black);
  }
  .about-title {
    position: absolute; left: 14px; top: 26px;
    font-family: "UnifrakturMaguntia", serif;
    font-weight: 400; font-size: 58px; line-height: 1;
    color: var(--heading-silver);
  }
  .about-copy {
    position: absolute; left: 33px; top: 131px;
    width: 312px;
    color: var(--body-text);
    font-size: 11px; line-height: 13.4px;
  }
  .about-copy p + p { margin-top: 13px; }
  .tagline {
    position: absolute; left: 303px; top: 540px;
    font-family: "Oswald", sans-serif;
    font-weight: 600; font-size: 42px; line-height: 1.1;
    letter-spacing: 2px;
    color: var(--tagline-grey);
    white-space: nowrap;
  }
</style>
</head>
<body>
  <div class="scene-backdrop" role="img" aria-label="Misty blue night forest with twisted trees, ravens and a gallows"></div>

  <nav class="top-bar">
    <a class="home-cross" href="#" style="left:385px" aria-label="Home">
      <svg width="10" height="14" viewBox="0 0 10 14"><rect x="4" y="0" width="2" height="14" fill="#d9d9d9"/><rect x="0.5" y="3.5" width="9" height="2" fill="#d9d9d9"/></svg>
    </a>
    <a href="#" style="left:491px">About Us</a>
    <a href="#" style="left:617px">Research</a>
    <a href="#" style="left:764px">Success Stories</a>
    <a href="#" style="left:888px">Gallery</a>
    <a href="#" style="left:993px">Contact</a>
  </nav>

  <div class="crest">
    <span class="crest-dot"></span>
    <span class="crest-name">DVK</span>
  </div>

  <div class="frame-ornament" role="img" aria-label="Ornate black scrollwork frame"></div>
  <section class="about-panel">
    <h1 class="about-title">About Us</h1>
    <div class="about-copy">
      <p>This text is for placement only. We are often asked to take people along with us on some our ghost hunting adventures. Our residential and private cases certainly do not allow us to do this but we do offer a great opportunity for the general public to take part in an evening of supernatural fun that helps to give back to organizations that are important to keeping haunted history alive. This text is for placement only.</p>
      <p>NIGHTWATCH - This text is for placement only.&nbsp; Ghost Hunting events are hosted by the Delta Spirit Research Team and our business associates to bring education and adventure to the novice or This text is for placement only. established ghost hunter. We host our events at different haunted locations throughout&nbsp; the south and tickets sells go to help with renovations, funding and educational programs per location.</p>
    </div>
  </section>

  <p class="tagline">dedicated to Paranormal research</p>
</body>
</html>
```